Plastering (solid plastering) business card design

We need a business card for a a small plastering business based in Perth Western Australia. We are a small team that provides a service in solid plastering specialising in float, white set and sand finish. We would like to see a clean business card with our name "Ridgeline Render Co" being the focus of the card and maybe incorporated into a logo. We don't have a logo at the moment so we would like to see some cards that may provide us with our future logo.

Industry/Entity Type

Business

Contact Information for Business Card

Ridgeline Render Co

Solid Plastering Specialists

Ph: Corey 0418730615
Ph: Luke 0451082963

Requirements
Should not have
• The design should not have Drywall incorporated into the card. In perth W.A. Plastering in different to someone that puts up Panelmax. We use sand, cement, lime and hardwall plaster.

```html
<!DOCTYPE html>
<html lang="en">
<head>
<meta charset="utf-8">
<title>Ridgeline Render Co — Business Card</title>
<link rel="stylesheet" href="https://fonts.googleapis.com/css2?family=Archivo+Black&family=Quicksand:wght@500;600&display=swap">
<style>
  :root {
    --backdrop: #d9d6d2;
    --card-white: #ffffff;
    --card-black: #0a0a0a;
    --orange: #f28a1e;
    --orange-deep: #e5601a;
    --ink: #111111;
    --text-light: #ffffff;
  }
  html, body {
    margin: 0;
    padding: 0;
    width: 1200px;
    height: 800px;
    overflow: hidden;
    background: var(--backdrop);
  }
  .business-card {
    position: absolute;
    left: 75px;
    top: 100px;
    width: 1050px;
    height: 600px;
    background: var(--card-white);
    overflow: hidden;
    box-shadow: 0 12px 30px rgba(0,0,0,0.25);
  }
  .card-shapes {
    position: absolute;
    inset: 0;
    width: 100%;
    height: 100%;
  }
  .brand {
    position: absolute;
    left: 300px;
    top: 70px;
    display: flex;
    align-items: center;
    gap: 26px;
  }
  .brand-dot {
    width: 120px;
    height: 120px;
    border-radius: 50%;
    background: var(--orange);
    flex: none;
  }
  .brand-name {
    margin: 0;
    font-family: "Archivo Black", sans-serif;
    font-weight: 400;
    font-size: 64px;
    line-height: 0.95;
    color: var(--ink);
    letter-spacing: -0.5px;
  }
  .contacts {
    position: absolute;
    left: 80px;
    top: 380px;
    font-family: "Quicksand", sans-serif;
    font-weight: 600;
  }
  .contact-line {
    display: flex;
    align-items: center;
    height: 58px;
  }
  .phone-icon {
    width: 40px;
    height: 40px;
    margin-right: 14px;
    flex: none;
  }
  .contact-name {
    width: 140px;
    font-size: 44px;
    color: var(--orange);
  }
  .contact-number {
    font-size: 44px;
    color: var(--text-light);
    letter-spacing: 1px;
  }
  .tagline {
    position: absolute;
    left: 90px;
    top: 528px;
    margin: 0;
    font-family: "Quicksand", sans-serif;
    font-weight: 600;
    font-size: 24px;
    letter-spacing: 0.62em;
    text-transform: uppercase;
    color: var(--orange);
  }
</style>
</head>
<body>
  <section class="business-card">
    <svg class="card-shapes" viewBox="0 0 1050 600" aria-hidden="true">
      <defs>
        <linearGradient id="swoosh-fill" x1="0" y1="0" x2="1" y2="0">
          <stop offset="0" stop-color="var(--orange-deep)"/>
          <stop offset="1" stop-color="var(--orange)"/>
        </linearGradient>
      </defs>
      <path class="accent-swoosh" d="M0 292 C140 345 300 378 520 372 C320 392 140 375 0 330 Z" fill="url(#swoosh-fill)"/>
      <path class="dark-band" d="M0 345 C200 400 420 405 620 372 C800 342 950 300 1050 292 L1050 600 L0 600 Z" fill="var(--card-black)"/>
    </svg>

    <div class="brand">
      <span class="brand-dot"></span>
      <h1 class="brand-name">Ridgeline<br>Render Co</h1>
    </div>

    <div class="contacts">
      <div class="contact-line">
        <svg class="phone-icon" viewBox="0 0 40 40" aria-hidden="true">
          <circle cx="20" cy="20" r="17" fill="none" stroke="var(--orange)" stroke-width="3"/>
          <path d="M13 12 l4 -1 l3 6 l-3 2 c1 3 3 5 6 6 l2 -3 l6 3 l-1 4 c-10 1 -18 -7 -17 -17 z" fill="var(--orange)"/>
        </svg>
        <span class="contact-name">Corey</span>
        <span class="contact-number">: 0418730615</span>
      </div>
      <div class="contact-line">
        <svg class="phone-icon" viewBox="0 0 40 40" aria-hidden="true">
          <circle cx="20" cy="20" r="17" fill="none" stroke="var(--orange)" stroke-width="3"/>
          <path d="M13 12 l4 -1 l3 6 l-3 2 c1 3 3 5 6 6 l2 -3 l6 3 l-1 4 c-10 1 -18 -7 -17 -17 z" fill="var(--orange)"/>
        </svg>
        <span class="contact-name">Luke</span>
        <span class="contact-number">: 0451082963</span>
      </div>
    </div>

    <p class="tagline">Solid Plastering Specialists</p>
  </section>
</body>
</html>
```